Editorial Website Design for High-End Custom Millwork Firm

Design (no development) for a 5-7 page website for a high-end custom architectural millwork firm. Editorial, magazine-quality aesthetic — think Dwelling Quarterly and top-tier millwork studios (Owen Tallard, Vorko). Full brief, reference sites, and project photography attached. We have uploaded a sample of our photography to use in your design. PLEASE READ PDF DOCUMENT BRIEF!!!

```html
<!DOCTYPE html>
<html lang="en">
<head>
<meta charset="utf-8">
<title>Commercial Projects Page – Alder Millwork</title>
<link href="https://fonts.googleapis.com/css2?family=EB+Garamond:wght@400;500&family=Inter:ital,wght@0,400;0,500;0,600;1,400&display=swap" rel="stylesheet">
<style>
:root{
  --board:#e3d5c3;
  --paper:#ffffff;
  --cream:#fbf4ec;
  --peach:#fbf1e6;
  --hero:#4a4a4a;
  --soft:#f6f6f6;
  --ink:#1f1f1f;
  --muted:#777;
  --footer:#1c1c1c;
  --footer-text:#bdb7ae;
  --gold:#cdbfa8;
  --btn:#ebe5dc;
  --menu:#d9d2c8;
  --serif:"EB Garamond", Georgia, serif;
  --sans:"Inter", Arial, sans-serif;
}
*{box-sizing:border-box;margin:0;padding:0}
html,body{width:1200px;height:3337px;overflow:hidden}
body{background:var(--board);font-family:var(--sans);color:var(--ink);position:relative}

.board-title{position:absolute;top:92px;left:0;width:1200px;text-align:center;font-family:var(--serif);font-size:30px;font-weight:400}
.comments{position:absolute;left:35px;top:157px;width:1058px;height:137px;background:var(--paper);display:flex;align-items:center;padding-left:52px}
.comments h2{font-family:var(--serif);font-weight:400;font-size:30px;margin-right:24px;margin-top:-8px}
.comments p{font-style:italic;font-size:12.5px;line-height:16px;width:760px;color:#222}

/* shared */
.label{font-size:5px;letter-spacing:.25em;text-transform:uppercase;color:#999}
.logo{font-family:var(--serif);letter-spacing:.18em;text-transform:uppercase;font-weight:400}
.photo{display:block}
.tone-a{background:linear-gradient(160deg,#7a5638 0%,#4a3726 45%,#2e2a28 75%,#56626a 100%)}
.tone-b{background:linear-gradient(170deg,#b0723f 0%,#8a5434 40%,#6a4a52 65%,#35548a 100%)}
.tone-c{background:linear-gradient(165deg,#8c6a45 0%,#c8a878 30%,#5a4632 60%,#1f1d1c 100%)}
.btn{display:inline-flex;align-items:center;gap:4px;background:var(--btn);font-size:5.5px;font-weight:600;letter-spacing:.12em;text-transform:uppercase;color:#222}
.btn svg{width:6px;height:6px}

/* desktop */
.desktop{position:absolute;left:189px;top:345px;width:576px;background:var(--paper)}
.d-nav{height:40px;background:var(--cream);display:flex;align-items:center;justify-content:space-between;padding:0 32px}
.d-nav .logo{font-size:17px}
.menu-btn{width:22px;height:22px;background:var(--menu);display:flex;align-items:center;justify-content:center}
.d-hero{height:188px;background:var(--hero);color:#fff;text-align:center;padding-top:65px}
.d-hero .label{color:#bbb}
.d-hero h1{font-family:var(--serif);font-weight:400;font-size:21px;margin:5px 0 12px}
.d-hero p{font-size:7px;color:#ccc;letter-spacing:.03em}
.d-gallery{height:606px;padding:33px 32px 0 33px}
.d-grid{display:grid;grid-template-columns:repeat(3,166px);grid-template-rows:repeat(3,174px);gap:8px}
.d-grid .tile{position:relative}
.tile-caption{position:absolute;inset:0;display:flex;flex-direction:column;align-items:center;justify-content:center;color:#fff;text-align:center}
.tile-caption h3{font-family:var(--serif);font-weight:400;font-size:13px}
.tile-caption span{font-size:5px;letter-spacing:.15em;text-transform:uppercase;margin-top:2px}
.d-process{height:249px;background:var(--soft);text-align:center;padding-top:45px}
.d-process h2{font-family:var(--serif);font-weight:400;font-size:20px;margin-top:5px}
.d-steps{display:flex;gap:8px;padding:0 32px 0 33px;margin-top:28px}
.d-steps .step{width:122px;height:100px;background:#fff;padding-top:10px}
.step.active{background:var(--peach)}
.step .num{font-family:var(--serif);font-size:15px}
.step h4{font-family:var(--serif);font-weight:500;font-size:7.5px;letter-spacing:.12em;margin:6px 0 5px}
.step p{font-size:5.5px;line-height:8px;color:#666;padding:0 18px}
.d-cta{height:188px;text-align:center;padding-top:52px}
.d-cta h2{font-family:var(--serif);font-weight:400;font-size:19px;letter-spacing:.02em}
.d-cta p{font-size:7px;line-height:11px;color:#666;margin:8px auto 10px;width:270px}
.d-cta .btn{padding:5px 9px}
.d-footer{height:306px;background:var(--footer);color:var(--footer-text);padding:48px 32px 0 31px;position:relative}
.d-footer .rule-top{position:absolute;left:31px;right:32px;top:48px;border-top:1px solid #2c2c2c}
.d-cols{display:flex;padding-top:36px}
.d-brand{width:225px}
.d-brand .logo{font-size:17px;color:var(--gold)}
.d-brand p{font-size:5.5px;line-height:8px;margin-top:10px;width:165px}
.socials{display:flex;gap:9px;margin-top:36px}
.socials i{width:9px;height:9px;border-radius:50%;background:#d8d2c9;display:block}
.f-col h5{font-family:var(--serif);font-weight:400;font-size:6.5px;letter-spacing:.22em;text-transform:uppercase;margin-bottom:12px}
.f-col ul{list-style:none}
.f-col li{font-size:5.5px;text-transform:uppercase;letter-spacing:.05em;color:#e6e0d7;margin-bottom:9.5px}
.f-col address{font-style:normal;font-size:5.5px;line-height:8px;text-transform:uppercase;letter-spacing:.05em}
.f-col .contact{font-size:5.5px;color:#e6e0d7;display:flex;align-items:center;gap:4px;margin-bottom:5px}
.f-col .contact svg{width:6px;height:6px}
.d-links{width:101px}.d-addr{width:100px}
.d-bottom{position:absolute;left:31px;right:32px;top:246px;border-top:1px solid #2c2c2c;display:flex;justify-content:space-between;padding:20px 5px 0;font-size:4.5px;letter-spacing:.15em;text-transform:uppercase}
.d-bottom span{display:flex;align-items:center;gap:5px}
.d-bottom svg{width:6px;height:6px}

/* mobile */
.mobile{position:absolute;left:771px;top:345px;width:156px;background:var(--paper)}
.m-nav{height:32px;background:var(--cream);display:flex;align-items:center;justify-content:space-between;padding:0 7px}
.m-nav .logo{font-size:11px}
.m-hero{height:189px;background:var(--hero);color:#fff;text-align:center;padding-top:40px}
.m-hero .label{color:#bbb}
.m-hero h1{font-family:var(--serif);font-weight:400;font-size:17px;line-height:18px;margin:7px 0 14px}
.m-hero p{font-size:7px;line-height:11px;color:#ccc;padding:0 12px}
.m-cards{height:1384px;padding:8px 7px 0;display:flex;flex-direction:column;gap:9px}
.m-card{height:141px;position:relative}
.m-card.tall{height:174px}
.m-card .tile-caption h3{font-size:13px;line-height:13px;width:110px}
.m-card .tile-caption span{margin:3px 0 8px}
.m-card .btn{background:#fff;width:110px;justify-content:center;padding:4px 0;font-size:5px}
.m-process{height:603px;background:var(--soft);text-align:center;padding-top:35px}
.m-process h2{font-family:var(--serif);font-weight:400;font-size:13px;margin-top:6px}
.m-steps{display:flex;flex-direction:column;gap:8px;padding:0 7px;margin-top:31px}
.m-steps .step{height:117px;background:#fff;padding-top:33px}
.m-steps .step p{padding:0 22px}
.m-cta{height:189px;text-align:center;padding-top:42px}
.m-cta h2{font-family:var(--serif);font-weight:400;font-size:13px;line-height:14px;padding:0 22px}
.m-cta p{font-size:7px;line-height:11px;color:#777;padding:0 18px;margin:8px 0 16px}
.m-cta .btn{padding:5px 9px;font-size:5px}
.m-footer{height:577px;background:var(--footer);color:var(--footer-text);text-align:center;padding-top:62px}
.m-footer .logo{font-size:13px;color:var(--gold)}
.m-footer .brand-text{font-size:5.5px;line-height:8px;padding:0 8px;margin-top:6px}
.m-footer .socials{justify-content:center;margin:10px 0 24px}
.m-block{border-top:1px solid #2e2e2e;padding:16px 0 14px}
.m-block h5{font-family:var(--serif);font-weight:400;font-size:6.5px;letter-spacing:.22em;text-transform:uppercase;margin-bottom:14px}
.m-block ul{list-style:none}
.m-block li{font-size:5.5px;text-transform:uppercase;color:#e6e0d7;margin-bottom:9.5px}
.m-block address{font-style:normal;font-size:5.5px;line-height:8px;text-transform:uppercase}
.m-block .contact{justify-content:center;font-size:5.5px;color:#e6e0d7;display:flex;align-items:center;gap:4px;margin-bottom:6px}
.m-block .contact svg{width:6px;height:6px}
.m-copy{border-top:1px solid #2e2e2e;padding-top:22px;font-size:4.5px;letter-spacing:.15em;text-transform:uppercase}
.m-copy span{display:flex;justify-content:center;align-items:center;gap:5px;margin-top:26px}
.m-copy svg{width:6px;height:6px}
</style>
</head>
<body>

<h1 class="board-title">Commercial Projects Page</h1>

<section class="comments">
  <h2>Comments:</h2>
  <p>The mobile version includes a “view detials” button&nbsp; on this so you can get an idea of what may look like. Please dol let me know what you think.</p>
</section>

<!-- Desktop layout -->
<main class="desktop">
  <header class="d-nav">
    <span class="logo">Alder Millwork</span>
    <span class="menu-btn"><svg width="11" height="9" viewBox="0 0 11 9"><path d="M0 1h11M0 3.7h11M0 6.3h11M3 9h8" stroke="#333" stroke-width="0.9"/></svg></span>
  </header>
  <section class="d-hero">
    <div class="label">— Our Work</div>
    <h1>Commercial Projects</h1>
    <p>All of our millwork is engineered, built, and finished at our facility in Ashford, NC</p>
  </section>
  <section class="d-gallery">
    <div class="d-grid">
      <div class="tile photo tone-a" role="img" aria-label="Hotel lobby with dark wood floor and black pendant lights">
        <div class="tile-caption"><h3>Harbor Lobby Retail</h3><span>Ashford, NC</span></div>
      </div>
      <div class="tile photo tone-b" role="img" aria-label="Lounge with wood-panelled ceiling, slatted screen and blue rug"></div>
      <div class="tile photo tone-c" role="img" aria-label="Retail boutique with arched lit shelving and oval display table"></div>
      <div class="tile photo tone-c" role="img" aria-label="Retail boutique with arched lit shelving and oval display table"></div>
      <div class="tile photo tone-c" role="img" aria-label="Retail boutique with arched lit shelving and oval display table"></div>
      <div class="tile photo tone-c" role="img" aria-label="Retail boutique with arched lit shelving and oval display table"></div>
      <div class="tile photo tone-c" role="img" aria-label="Retail boutique with arched lit shelving and oval display table"></div>
      <div class="tile photo tone-c" role="img" aria-label="Retail boutique with arched lit shelving and oval display table"></div>
      <div class="tile photo tone-c" role="img" aria-label="Retail boutique with arched lit shelving and oval display table"></div>
    </div>
  </section>
  <section class="d-process">
    <div class="label">— Alder Millwork Process</div>
    <h2>Our Craft Process</h2>
    <div class="d-steps">
      <div class="step"><div class="num">01</div><h4>Engineering</h4><p>Collaborative conceptualization ensuring architectural intent is perfectly captured.</p></div>
      <div class="step active"><div class="num">02</div><h4>Fabrication</h4><p>State-of-the-art manufacturing combined with traditional hand-crafted techniques.</p></div>
      <div class="step"><div class="num">03</div><h4>Finishing</h4><p>Bespoke hand-applied finishes ranging from natural oils to high-gloss lacquers.</p></div>
      <div class="step" style="padding-top:18px"><div class="num">04</div><h4>Installation</h4><p>White-glove installation teams ensuring millimetric precision on-site.</p></div>
    </div>
  </section>
  <section class="d-cta">
    <h2>Have A Project In Mind?</h2>
    <p>We work closely with architects and designers from concept through installation to bring vision into reality.</p>
    <span class="btn">Start a Conversation <svg viewBox="0 0 8 8"><path d="M1 4h6M4.5 1.5 7 4 4.5 6.5" fill="none" stroke="#222" stroke-width="1"/></svg></span>
  </section>
  <footer class="d-footer">
    <div class="rule-top"></div>
    <div class="d-cols">
      <div class="d-brand">
        <div class="logo">Alder Millwork</div>
        <p>Alder Millwork partners with the top designers and architects on the East Coast to produce and install award-quality millwork in residential and commercial environments.</p>
        <div class="socials"><i></i><i></i><i></i><i></i></div>
      </div>
      <div class="f-col d-links">
        <h5>Quick Links</h5>
        <ul><li>Home</li><li>About</li><li>Projects</li><li>Millwork Design</li><li>Residential</li><li>Contact</li></ul>
      </div>
      <div class="f-col d-addr">
        <h5>Address</h5>
        <address>Alder Architectural<br>Millwork,<br>118 Linden Row<br>Ashford, NC 27510</address>
      </div>
      <div class="f-col">
        <h5>Get In Touch</h5>
        <div class="contact"><svg viewBox="0 0 8 8"><path d="M1.5 1 3 1 3.6 2.8 2.7 3.5Q3.6 5 4.6 5.4L5.3 4.6 7 5.1 7 6.6Q3 7 1.2 2.2Z" fill="none" stroke="#ddd" stroke-width=".7"/></svg>555.201.4830</div>
        <div class="contact"><svg viewBox="0 0 8 8"><circle cx="4" cy="4" r="3" fill="none" stroke="#ddd" stroke-width=".7"/><path d="M4 2.3v1.9l1.2.8" stroke="#ddd" stroke-width=".7" fill="none"/></svg>555.201.4862</div>
        <div class="contact" style="margin-top:12px"><svg viewBox="0 0 8 8"><rect x=".8" y="1.8" width="6.4" height="4.4" fill="none" stroke="#ddd" stroke-width=".7"/><path d="M.8 1.8 4 4.4 7.2 1.8" fill="none" stroke="#ddd" stroke-width=".7"/></svg>hello@aldermillwork.com</div>
      </div>
    </div>
    <div class="d-bottom">
      <span>Copyright © 2026 Alder. All rights reserved.</span>
      <span>Back to top <svg viewBox="0 0 8 8"><path d="M4 7V1M1.5 3.5 4 1l2.5 2.5" fill="none" stroke="#ddd" stroke-width=".9"/></svg></span>
    </div>
  </footer>
</main>

<!-- Mobile layout -->
<main class="mobile">
  <header class="m-nav">
    <span class="logo">Alder Millwork</span>
    <svg width="11" height="8" viewBox="0 0 11 8"><path d="M0 .5h11M0 3h11M0 5.5h11M3 8h8" stroke="#333" stroke-width="0.8"/></svg>
  </header>
  <section class="m-hero">
    <div class="label">— Our Work</div>
    <h1>Residential<br>Projects</h1>
    <p>All of our millwork is engineered, built, and finished at our facility in Ashford, NC</p>
  </section>
  <section class="m-cards">
    <div class="m-card photo tone-a" role="img" aria-label="Hotel lobby with dark wood floor and black pendant lights"><div class="tile-caption"><h3>Harbor Lobby Retail</h3><span>Ashford, NC</span><span class="btn">View Details <svg viewBox="0 0 8 8"><path d="M1 4h6M4.5 1.5 7 4 4.5 6.5" fill="none" stroke="#222" stroke-width="1"/></svg></span></div></div>
    <div class="m-card photo tone-b" role="img" aria-label="Lounge with wood-panelled ceiling, slatted screen and blue rug"><div class="tile-caption"><h3>Harbor Lobby Retail</h3><span>Ashford, NC</span><span class="btn">View Details <svg viewBox="0 0 8 8"><path d="M1 4h6M4.5 1.5 7 4 4.5 6.5" fill="none" stroke="#222" stroke-width="1"/></svg></span></div></div>
    <div class="m-card photo tone-c" role="img" aria-label="Retail boutique with arched lit shelving and oval display table"><div class="tile-caption"><h3>Harbor Lobby Retail</h3><span>Ashford, NC</span><span class="btn">View Details <svg viewBox="0 0 8 8"><path d="M1 4h6M4.5 1.5 7 4 4.5 6.5" fill="none" stroke="#222" stroke-width="1"/></svg></span></div></div>
    <div class="m-card tall photo tone-c" role="img" aria-label="Retail boutique with arched lit shelving and oval display table"><div class="tile-caption"><h3>Harbor Lobby Retail</h3><span>Ashford, NC</span><span class="btn">View Details <svg viewBox="0 0 8 8"><path d="M1 4h6M4.5 1.5 7 4 4.5 6.5" fill="none" stroke="#222" stroke-width="1"/></svg></span></div></div>
    <div class="m-card photo tone-c" role="img" aria-label="Retail boutique with arched lit shelving and oval display table"><div class="tile-caption"><h3>Harbor Lobby Retail</h3><span>Ashford, NC</span><span class="btn">View Details <svg viewBox="0 0 8 8"><path d="M1 4h6M4.5 1.5 7 4 4.5 6.5" fill="none" stroke="#222" stroke-width="1"/></svg></span></div></div>
    <div class="m-card photo tone-c" role="img" aria-label="Retail boutique with arched lit shelving and oval display table"><div class="tile-caption"><h3>Harbor Lobby Retail</h3><span>Ashford, NC</span><span class="btn">View Details <svg viewBox="0 0 8 8"><path d="M1 4h6M4.5 1.5 7 4 4.5 6.5" fill="none" stroke="#222" stroke-width="1"/></svg></span></div></div>
    <div class="m-card photo tone-c" role="img" aria-label="Retail boutique with arched lit shelving and oval display table"><div class="tile-caption"><h3>Harbor Lobby Retail</h3><span>Ashford, NC</span><span class="btn">View Details <svg viewBox="0 0 8 8"><path d="M1 4h6M4.5 1.5 7 4 4.5 6.5" fill="none" stroke="#222" stroke-width="1"/></svg></span></div></div>
    <div class="m-card photo tone-c" role="img" aria-label="Retail boutique with arched lit shelving and oval display table"><div class="tile-caption"><h3>Harbor Lobby Retail</h3><span>Ashford, NC</span><span class="btn">View Details <svg viewBox="0 0 8 8"><path d="M1 4h6M4.5 1.5 7 4 4.5 6.5" fill="none" stroke="#222" stroke-width="1"/></svg></span></div></div>
    <div class="m-card photo tone-c" role="img" aria-label="Retail boutique with arched lit shelving and oval display table"><div class="tile-caption"><h3>Harbor Lobby Retail</h3><span>Ashford, NC</span><span class="btn">View Details <svg viewBox="0 0 8 8"><path d="M1 4h6M4.5 1.5 7 4 4.5 6.5" fill="none" stroke="#222" stroke-width="1"/></svg></span></div></div>
  </section>
  <section class="m-process">
    <div class="label">— Alder Millwork Process</div>
    <h2>Our Craft Process</h2>
    <div class="m-steps">
      <div class="step"><div class="num">01</div><h4>Engineering</h4><p>Collaborative conceptualization ensuring architectural intent is perfectly captured.</p></div>
      <div class="step"><div class="num">02</div><h4>Fabrication</h4><p>State-of-the-art manufacturing combined with traditional hand-crafted techniques.</p></div>
      <div class="step" style="padding-top:26px"><div class="num">03</div><h4>Finishing</h4><p>Bespoke hand-applied finishes ranging from natural oils to high-gloss lacquers.</p></div>
      <div class="step"><div class="num">04</div><h4>Installation</h4><p>White-glove installation teams ensuring millimetric precision on-site.</p></div>
    </div>
  </section>
  <section class="m-cta">
    <h2>Have A Project In Mind?</h2>
    <p>We work closely with architects and designers from concept through installation to bring vision into reality.</p>
    <span class="btn">Start a Conversation <svg viewBox="0 0 8 8"><path d="M1 4h6M4.5 1.5 7 4 4.5 6.5" fill="none" stroke="#222" stroke-width="1"/></svg></span>
  </section>
  <footer class="m-footer">
    <div class="logo">Alder Millwork</div>
    <p class="brand-text">Alder Millwork partners with the top designers and architects on the East Coast to produce and install award-quality millwork in residential and commercial environments.</p>
    <div class="socials"><i></i><i></i><i></i><i></i></div>
    <div class="m-block">
      <h5>Quick Links</h5>
      <ul><li>Home</li><li>About</li><li>Projects</li><li>Millwork Design</li><li>Residential</li><li>Contact</li></ul>
    </div>
    <div class="m-block">
      <h5>Address</h5>
      <address>Alder Architectural Millwork,<br>118 Linden Row<br>Ashford, NC 27510</address>
    </div>
    <div class="m-block">
      <h5>Get In Touch</h5>
      <div class="contact"><svg viewBox="0 0 8 8"><path d="M1.5 1 3 1 3.6 2.8 2.7 3.5Q3.6 5 4.6 5.4L5.3 4.6 7 5.1 7 6.6Q3 7 1.2 2.2Z" fill="none" stroke="#ddd" stroke-width=".7"/></svg>555.201.4830</div>
      <div class="contact"><svg viewBox="0 0 8 8"><circle cx="4" cy="4" r="3" fill="none" stroke="#ddd" stroke-width=".7"/><path d="M4 2.3v1.9l1.2.8" stroke="#ddd" stroke-width=".7" fill="none"/></svg>555.201.4862</div>
      <div class="contact" style="margin-top:14px"><svg viewBox="0 0 8 8"><rect x=".8" y="1.8" width="6.4" height="4.4" fill="none" stroke="#ddd" stroke-width=".7"/><path d="M.8 1.8 4 4.4 7.2 1.8" fill="none" stroke="#ddd" stroke-width=".7"/></svg>hello@aldermillwork.com</div>
    </div>
    <div class="m-copy">
      Copyright © 2026 Alder. All rights reserved.
      <span>Back to top <svg viewBox="0 0 8 8"><path d="M4 7V1M1.5 3.5 4 1l2.5 2.5" fill="none" stroke="#ddd" stroke-width=".9"/></svg></span>
    </div>
  </footer>
</main>

</body>
</html>
```